Plovanta medical teaching of the future

responsive website, onepager, for medical technology company. It has to look clean and high tech.

Look & feel
• Responsive
• Clean
• Combination icons + foto's
• Integration of a YouTube video

Landingpage items

• Header: picture + 'a video-based teaching platform for surgical procedures'
• About Deferred live medical teaching: Short description
• Features
o Video
o Teaching platform

• Benefits:
o More effective learning
o Faster sharing of knowledge & tecniques
o More cost effective

• References

• Products:
o Live (+link to more info)
o Qorvex (+ link to more info)
o Qorvex local (+link to more info)
o Qorvex cloud (+ link to more info)

• Solutions:
o For medical device companies (+link to more info)
o Doctor and surgeons (+link to more info)
o Medical conferences (+link to more info)

Target Market(s)

medical device companies
surgeons and doctors
conference organisers

Industry/Entity Type

It Company

Number of Pages Required

1 page

Requirements
Must have
• Landingpage items
• • Header: picture + 'a video-based teaching platform for surgical procedures'
• • About Deferred live medical teaching: Short description
• • Features
• o Video
• o Teaching platform
• • Benefits:
• o More effective learning
• o Faster sharing of knowledge & tecniques
• o More cost effective
• • References
• • Products:
• o Live (+link to more info)
• o Qorvex (+ link to more info)
• o Qorvex local (+link to more info)
• o Qorvex cloud (+ link to more info)
• • Solutions:
• o For medical device companies (+link to more info)
• o Doctor and surgeons (+link to more info)
• o Medical conferences (+link to more info)
Nice to have
• possibilty to show video

```html
<!DOCTYPE html>
<html lang="en">
<head>
<meta charset="utf-8">
<title>Plovanta – medical teaching of the future</title>
<link href="https://fonts.googleapis.com/css2?family=Montserrat:wght@400;600;700&family=Open+Sans:wght@400;600;700&display=swap" rel="stylesheet">
<style>
:root{
  --teal:#27a39b;
  --teal-dark:#1f8a83;
  --red:#e8464b;
  --ink:#333333;
  --muted:#777777;
  --light:#ededed;
  --line:#dddddd;
  --white:#ffffff;
}
*{box-sizing:border-box;margin:0;padding:0}
html,body{width:1200px;height:4128px;overflow:hidden}
body{font-family:"Open Sans",Arial,sans-serif;color:var(--ink);background:var(--white);font-size:15px;line-height:1.6}
.wrap{width:1040px;margin:0 auto;position:relative;height:100%}

/* top bar */
.topbar{height:48px;background:#f4f4f4;border-bottom:1px solid var(--line)}
.topbar .wrap{display:flex;justify-content:flex-end;align-items:center;gap:10px}
.dot{width:16px;height:16px;border-radius:50%;background:#c8c8c8}
.login{background:var(--teal);color:var(--white);font-size:12px;font-weight:600;padding:6px 16px;margin-left:12px}

/* header */
.header{height:104px}
.header .wrap{display:flex;align-items:center;justify-content:space-between}
.brand{display:flex;align-items:center;gap:14px}
.brand-mark{width:44px;height:44px;border-radius:50%;background:var(--teal)}
.brand-name{font-family:"Montserrat",sans-serif;font-weight:700;font-size:42px;color:var(--teal);letter-spacing:-1px}
.contact{display:flex;gap:60px}
.contact-item{display:flex;gap:12px;align-items:center;font-size:13px;line-height:1.5;color:var(--muted)}
.contact-item strong{display:block;color:var(--ink);font-size:15px;font-weight:600}

/* nav */
.nav{height:48px;background:var(--teal)}
.nav ul{list-style:none;display:flex;height:48px}
.nav li{font-family:"Montserrat",sans-serif;font-size:13px;font-weight:600;color:var(--white);padding:0 22px;line-height:48px}
.nav li.active{background:var(--red)}

/* hero */
.hero{height:540px;position:relative;background:linear-gradient(135deg,#5d7276 0%,#8aa3a6 35%,#4c6063 70%,#2f3d40 100%)}
.hero-text{position:absolute;top:140px;left:0;width:100%;text-align:center;color:var(--white);font-family:"Open Sans",sans-serif;font-weight:700;font-size:44px;line-height:1.3}
.play{position:absolute;width:84px;height:84px;border-radius:50%;background:var(--red);display:flex;align-items:center;justify-content:center}
.hero .play{left:558px;top:300px}

/* about */
.about{height:600px}
.about .wrap{display:flex;gap:40px;padding-top:100px}
.about-photos{width:420px;height:380px;position:relative;flex:none}
.ph{position:absolute}
.ph-a{left:0;top:0;width:260px;height:200px;background:linear-gradient(135deg,#9fb8bb,#5c7377)}
.ph-b{left:180px;top:140px;width:240px;height:240px;background:linear-gradient(135deg,#c6cfd1,#6f8184);border:6px solid var(--white)}
.ph-c{left:20px;top:220px;width:170px;height:150px;background:linear-gradient(135deg,#8da3a6,#3e5054)}
.about-text{flex:1}
.section-title{font-family:"Montserrat",sans-serif;font-weight:700;font-size:34px;color:var(--teal);margin-bottom:14px}
.about-text p{font-size:14px;color:var(--muted);margin-bottom:14px}
.about-text h4{font-size:15px;font-weight:700;margin-bottom:4px}
.btn{display:inline-block;font-family:"Montserrat",sans-serif;font-size:12px;font-weight:600;color:var(--white);background:var(--red);padding:10px 22px}
.btn-grey{background:#c9c9c9;color:var(--ink)}

/* platform */
.platform{height:500px;position:relative;background:linear-gradient(135deg,#9a9a9a,#6d6d6d 50%,#8d8d8d)}
.platform .wrap{display:flex;justify-content:space-between;padding-top:90px}
.platform-list h3{font-family:"Montserrat",sans-serif;font-weight:700;font-size:34px;color:var(--white);margin-bottom:16px}
.platform-list ul{list-style:none}
.platform-list li{color:var(--white);font-size:14px;line-height:30px;padding-left:18px;position:relative}
.platform-list li::before{content:"";position:absolute;left:0;top:13px;width:6px;height:6px;background:var(--white);border-radius:50%}
.video{width:540px;height:330px;position:relative;background:linear-gradient(135deg,#7fa0a3,#3f5a5e);border:6px solid var(--white)}
.video .play{left:222px;top:117px}

/* benefits */
.benefits{height:740px;background:var(--light)}
.heading-center{font-family:"Montserrat",sans-serif;font-weight:700;font-size:40px;text-align:center;padding-top:70px;margin-bottom:40px}
.cards{display:flex;gap:25px}
.card{width:330px;background:var(--white)}
.card-photo{height:180px}
.card-body{padding:20px 22px 24px}
.card h3{font-family:"Montserrat",sans-serif;font-size:20px;font-weight:700;margin-bottom:8px}
.card p{font-size:13px;color:var(--muted);margin-bottom:18px}
.card .btn{display:block;text-align:center}

/* products */
.products{height:540px}
.products .heading-center{padding-top:60px;margin-bottom:50px}
.product-row{display:flex;gap:40px}
.product{width:230px;text-align:center}
.product-img{height:130px;margin-bottom:18px;background:linear-gradient(180deg,#9a9a9a,#3e3e3e);border-radius:6px}
.product h3{font-family:"Montserrat",sans-serif;font-size:22px;font-weight:700;margin-bottom:8px}
.product p{font-size:13px;color:var(--muted);margin-bottom:8px}
.more{font-size:12px;color:var(--red);font-weight:600}

/* solution */
.solution{height:620px;background:var(--light)}
.solution .heading-center{padding-top:40px;margin-bottom:30px}
.sol-grid{display:flex;gap:20px}
.sol-main{width:520px;background:var(--white)}
.sol-main .sol-photo{height:240px;background:linear-gradient(135deg,#b7c7ca,#5f7478)}
.sol-main .sol-body{padding:20px 24px}
.sol-side{width:500px;display:flex;flex-direction:column;gap:20px}
.sol-card{background:var(--white);display:flex;height:220px}
.sol-card .sol-photo{width:190px;flex:none;background:linear-gradient(135deg,#d4dadb,#8e9c9e)}
.sol-card .sol-body{padding:18px 20px;flex:1;position:relative}
.sol-body h3{font-family:"Montserrat",sans-serif;font-size:20px;font-weight:700;margin-bottom:8px}
.sol-body p{font-size:13px;color:var(--muted)}
.sol-main .btn{display:block;text-align:center;margin-top:18px}
.sol-card .btn{position:absolute;right:0;bottom:0;left:0;text-align:right}

/* footer */
.footer{height:388px;background:var(--teal);color:var(--white);text-align:center;padding-top:80px}
.footer .brand{justify-content:center}
.footer .brand-mark{background:var(--white)}
.footer .brand-name{color:var(--white)}
.footer-nav{list-style:none;display:flex;justify-content:center;gap:26px;margin-top:40px;font-family:"Montserrat",sans-serif;font-size:13px;font-weight:600}
.copy{font-size:12px;margin-top:16px;opacity:.85}
.socials{display:flex;justify-content:center;gap:12px;margin-top:22px}
.socials span{width:30px;height:30px;border-radius:50%;background:var(--teal-dark);border:2px solid var(--white)}
</style>
</head>
<body>

<div class="topbar"><div class="wrap">
  <span class="dot"></span><span class="dot"></span><span class="dot"></span><span class="dot"></span>
  <span class="login">Distributor Login</span>
</div></div>

<header class="header"><div class="wrap">
  <div class="brand"><span class="brand-mark"></span><span class="brand-name">Plovanta</span></div>
  <div class="contact">
    <div class="contact-item">
      <svg width="28" height="28" viewBox="0 0 24 24"><path fill="#27a39b" d="M6.6 10.8a15 15 0 0 0 6.6 6.6l2.2-2.2c.3-.3.7-.4 1-.2 1.1.4 2.3.6 3.6.6.6 0 1 .4 1 1V20c0 .6-.4 1-1 1A17 17 0 0 1 3 4c0-.6.4-1 1-1h3.5c.6 0 1 .4 1 1 0 1.3.2 2.5.6 3.6.1.3 0 .7-.2 1z"/></svg>
      <div><strong>1 800 555 0142</strong>info@plovanta-med.com</div>
    </div>
    <div class="contact-item">
      <svg width="28" height="28" viewBox="0 0 24 24"><circle cx="12" cy="12" r="10" fill="none" stroke="#27a39b" stroke-width="2"/><path d="M12 6v6l4 2" fill="none" stroke="#27a39b" stroke-width="2"/></svg>
      <div><strong>7:30 AM - 7:30 PM</strong>Monday to Saturday</div>
    </div>
  </div>
</div></header>

<nav class="nav"><div class="wrap"><ul>
  <li class="active">HOME</li><li>ABOUT US</li><li>FEATURES</li><li>BENEFITS</li><li>REFERENCES</li><li>PRODUCTS</li><li>SOLUTIONS</li><li>CONTACT</li>
</ul></div></nav>

<section class="hero" role="img" aria-label="Surgical team performing a procedure in an operating room">
  <h1 class="hero-text">Plovanta changes the way medical<br>procedures are taught</h1>
  <span class="play"><svg width="32" height="32" viewBox="0 0 24 24"><path d="M7 4l13 8-13 8z" fill="#fff"/></svg></span>
</section>

<section class="about"><div class="wrap">
  <div class="about-photos">
    <div class="ph ph-a" role="img" aria-label="Surgeons at work under operating lights"></div>
    <div class="ph ph-c" role="img" aria-label="Video recording equipment in theatre"></div>
    <div class="ph ph-b" role="img" aria-label="Medical monitors in an operating room"></div>
  </div>
  <div class="about-text">
    <h2 class="section-title">About Plovanta</h2>
    <p>Medical device companies, doctors and surgeons all over the world develop new or breakthrough products, medical and surgical techniques. These techniques save lives or increase the survival rate of many patients.</p>
    <p>It is therefore very important that these companies, doctors and surgeons share their knowledge as fast and accurately as possible. The current methods to share this knowledge are peer-to-peer live teaching and live medical teaching at conferences.</p>
    <h4>Peer-to-peer live medical teaching</h4>
    <p>Healthcare companies contract top surgeons to do teaching sessions with their appliances and equipment. In the case of peer-to-peer teaching, companies fly in surgeons from all over the world to attend the sessions.</p>
    <span class="btn">MORE DETAILS</span>
  </div>
</div></section>

<section class="platform" role="img" aria-label="Dimmed operating room scene in the background">
  <div class="wrap">
    <div class="platform-list">
      <h3>Teaching platform</h3>
      <ul>
        <li>Live streaming of surgical procedures</li>
        <li>Recorded sessions for later review</li>
        <li>Multi-camera operating room capture</li>
        <li>Expert commentary and annotations</li>
        <li>Secure cloud video library</li>
        <li>Interactive questions for trainees</li>
        <li>Ready for conference broadcasts</li>
      </ul>
    </div>
    <div class="video" role="img" aria-label="Video preview of a surgical procedure">
      <span class="play"><svg width="32" height="32" viewBox="0 0 24 24"><path d="M7 4l13 8-13 8z" fill="#fff"/></svg></span>
    </div>
  </div>
</section>

<section class="benefits"><div class="wrap">
  <h2 class="heading-center">Benefits</h2>
  <div class="cards">
    <article class="card">
      <div class="card-photo" role="img" aria-label="Group of students learning together" style="background:linear-gradient(135deg,#c9b9a4,#7d8a99)"></div>
      <div class="card-body">
        <h3>More effective learning</h3>
        <p>Medical device companies, doctors and surgeons all over the world develop new or breakthrough products, medical and surgical techniques. These techniques save lives or increase the survival rate of many patients.</p>
        <span class="btn">Read More</span>
      </div>
    </article>
    <article class="card">
      <div class="card-photo" role="img" aria-label="Medical team discussing around a table" style="background:linear-gradient(135deg,#b9c9d4,#6f8797)"></div>
      <div class="card-body">
        <h3>Faster sharing &amp; tecniques</h3>
        <p>Medical device companies, doctors and surgeons all over the world develop new or breakthrough products, medical and surgical techniques. These techniques help to increase the results.</p>
        <span class="btn btn-grey">Read More</span>
      </div>
    </article>
    <article class="card">
      <div class="card-photo" role="img" aria-label="Doctor working on a laptop" style="background:linear-gradient(135deg,#d4d7db,#8a96a3)"></div>
      <div class="card-body">
        <h3>More Cost Effective</h3>
        <p>Medical device companies, doctors and surgeons all over the world develop new or breakthrough products, medical and surgical techniques.</p>
        <span class="btn btn-grey">Read More</span>
      </div>
    </article>
  </div>
</div></section>

<section class="products"><div class="wrap">
  <h2 class="heading-center">Benefits</h2>
  <div class="product-row">
    <div class="product">
      <div class="product-img" role="img" aria-label="Live video capture unit"></div>
      <h3>Live</h3>
      <p>Medical device companies, doctors and surgeons all over the world share surgical techniques.</p>
      <span class="more">+ more info</span>
    </div>
    <div class="product">
      <div class="product-img" role="img" aria-label="Qorvex control console"></div>
      <h3>o Qorvex</h3>
      <p>Medical device companies, doctors and surgeons all over the world share surgical techniques.</p>
      <span class="more">+ more info</span>
    </div>
    <div class="product">
      <div class="product-img" role="img" aria-label="Qorvex local capture unit"></div>
      <h3>o Qorvex local</h3>
      <p>Medical device companies, doctors and surgeons all over the world share surgical techniques.</p>
      <span class="more">+ more info</span>
    </div>
    <div class="product">
      <div class="product-img" role="img" aria-label="Qorvex cloud console"></div>
      <h3>o Qorvex cloud</h3>
      <p>Medical device companies, doctors and surgeons all over the world share surgical techniques.</p>
      <span class="more">+ more info</span>
    </div>
  </div>
</div></section>

<section class="solution"><div class="wrap">
  <h2 class="heading-center">Solution</h2>
  <div class="sol-grid">
    <article class="sol-main">
      <div class="sol-photo" role="img" aria-label="Hybrid operating room with imaging equipment"></div>
      <div class="sol-body">
        <h3>For Medical Device Companies</h3>
        <p>It is therefore very important that these medical device companies, doctors and surgeons share their knowledge as fast and accurately as possible. The current methods to share this knowledge are peer-to-peer live teaching and live medical teaching at conferences.</p>
        <p>Medical device companies, doctors and surgeons all over the world develop new or breakthrough products.</p>
        <span class="btn btn-grey">+ More info</span>
      </div>
    </article>
    <div class="sol-side">
      <article class="sol-card">
        <div class="sol-photo" role="img" aria-label="Doctor and surgeons team portrait"></div>
        <div class="sol-body">
          <h3>Doctor &amp; surgeons</h3>
          <p>It is therefore very important that these medical device companies, doctors and surgeons share their knowledge as fast as possible.</p>
          <span class="btn">+ More info</span>
        </div>
      </article>
      <article class="sol-card">
        <div class="sol-photo" role="img" aria-label="Medical team at a conference"></div>
        <div class="sol-body">
          <h3>Medical conferences</h3>
          <p>It is therefore very important that these medical device companies, doctors and surgeons share their knowledge as fast as possible.</p>
          <span class="btn">+ More info</span>
        </div>
      </article>
    </div>
  </div>
</div></section>

<footer class="footer">
  <div class="brand"><span class="brand-mark"></span><span class="brand-name">Plovanta</span></div>
  <ul class="footer-nav">
    <li>HOME</li><li>ABOUT US</li><li>FEATURES</li><li>BENEFITS</li><li>REFERENCES</li><li>PRODUCTS</li><li>SOLUTIONS</li><li>CONTACT</li>
  </ul>
  <p class="copy">Copyright © 2016 Plovanta (Norvale Medical). All rights reserved.</p>
  <div class="socials"><span></span><span></span><span></span><span></span></div>
</footer>

</body>
</html>
```